this is a new company aimed at the automotive glass industry
what we do is repair cracked windscreens its based in western austraila
I like the old dragracing signwritting logos
I want it to stand out thats why ive gone with the name and title
I dont have a logo but if you can think of one that would be great
but not essential
on the back of the business card i would like Quicker Cheaper Better

Reason: More time needed to decide some great designs Have come through on the eleventh

Target Market(s)

automotive (car yards ,car auctions , trucking companys ect )

Industry/Entity Type

Automotive

Contact Information for Business Card

Pane Stoppers ,
Glass Crack repair specialists ,
Dorian Pelletier ,0437 612 084 ,dpelletier@panestopperswa.com.au

```html
<!DOCTYPE html>
<html lang="en">
<head>
<meta charset="utf-8">
<title>Pane Stoppers – Business Card</title>
<link rel="stylesheet" href="https://fonts.googleapis.com/css2?family=Oswald:wght@400;500;600&display=swap">
<style>
  :root {
    --page-bg: #e9e6e1;
    --card-black: #0b0b0c;
    --card-charcoal: #1c1d1f;
    --glass-light: #c9ccd0;
    --glass-mid: #6d7074;
    --steel-blue: #7db3c6;
    --text-white: #f2f2f2;
    --tagline-grey: #d6d8da;
  }
  html, body {
    margin: 0;
    width: 1200px;
    height: 784px;
    overflow: hidden;
    background: var(--page-bg);
    font-family: "Oswald", "Arial Narrow", sans-serif;
  }
  .sheet {
    position: relative;
    width: 1200px;
    height: 784px;
  }
  .card {
    position: absolute;
    width: 540px;
    height: 310px;
    border-radius: 4px;
    overflow: hidden;
    box-shadow: 0 10px 28px rgba(0,0,0,0.25);
    background: var(--card-black);
  }
  /* Back of card */
  .card-back {
    left: 40px;
    top: 237px;
  }
  .card-back .photo-area {
    position: absolute;
    left: 16px;
    top: 14px;
    right: 16px;
    bottom: 56px;
    background:
      radial-gradient(ellipse at 35% 40%, var(--glass-light) 0%, var(--glass-mid) 35%, transparent 70%),
      radial-gradient(ellipse at 75% 30%, #9a9da1 0%, transparent 55%),
      linear-gradient(160deg, #3a3c3f 0%, #141516 100%);
  }
  .card-back .slogan {
    position: absolute;
    left: 0;
    right: 0;
    bottom: 18px;
    display: flex;
    justify-content: space-around;
    padding: 0 30px;
    color: var(--text-white);
    font-size: 15px;
    font-weight: 400;
    letter-spacing: 0.6em;
    text-transform: uppercase;
  }
  /* Front of card */
  .card-front {
    left: 620px;
    top: 237px;
  }
  .card-front .shatter-area {
    position: absolute;
    inset: 0;
    background:
      radial-gradient(ellipse at 30% 45%, rgba(120,124,128,0.45) 0%, transparent 45%),
      radial-gradient(ellipse at 85% 35%, rgba(140,144,148,0.35) 0%, transparent 40%),
      linear-gradient(150deg, var(--card-charcoal) 0%, var(--card-black) 70%);
  }
  .card-front .content {
    position: absolute;
    inset: 0;
  }
  .brand-name {
    position: absolute;
    left: 44px;
    top: 36px;
    margin: 0;
    color: var(--steel-blue);
    font-size: 56px;
    font-weight: 600;
    line-height: 1;
    letter-spacing: 0.06em;
    text-transform: uppercase;
  }
  .brand-tagline {
    position: absolute;
    left: 48px;
    top: 104px;
    margin: 0;
    color: var(--tagline-grey);
    font-size: 13px;
    font-weight: 500;
    letter-spacing: 0.38em;
    text-transform: uppercase;
  }
  .contact-name {
    position: absolute;
    left: 210px;
    top: 150px;
    margin: 0;
    color: var(--steel-blue);
    font-size: 19px;
    font-weight: 500;
    letter-spacing: 0.04em;
    text-transform: uppercase;
  }
  .contact-phone {
    position: absolute;
    left: 206px;
    top: 196px;
    margin: 0;
    color: var(--text-white);
    font-size: 26px;
    font-weight: 500;
    letter-spacing: 0.12em;
  }
  .contact-email {
    position: absolute;
    left: 120px;
    top: 246px;
    margin: 0;
    color: var(--text-white);
    font-size: 15px;
    font-weight: 400;
    letter-spacing: 0.16em;
    text-transform: uppercase;
  }
</style>
</head>
<body>
  <main class="sheet">
    <section class="card card-back" aria-label="Business card back">
      <div class="photo-area" role="img" aria-label="Close-up photograph of clear broken glass fragments on black"></div>
      <p class="slogan"><span>Quicker</span><span>Cheaper</span><span>Better</span></p>
    </section>

    <section class="card card-front" aria-label="Business card front">
      <div class="shatter-area" role="img" aria-label="Photograph of shattering glass shards on a black background"></div>
      <div class="content">
        <h1 class="brand-name">Pane Stoppers</h1>
        <p class="brand-tagline">Glass Crack Repair Specialist</p>
        <p class="contact-name">Dorian Pelletier</p>
        <p class="contact-phone">0437 612 084</p>
        <p class="contact-email">dpelletier@panestopperswa.com.au</p>
      </div>
    </section>
  </main>
</body>
</html>
```